Business Card Design Project

We need a business card for our IT services provider business. We provide services to small and medium business, and would like something that reflects the color scheme / branding on our recently updated website - www.tallobrix.com.au

The card type we have chosen is a matte laminated double sided configuration at 86mm x 54mm on 350 GSM cardboard.
Updates

Target Market(s)

Small and Medium Business owners

Industry/Entity Type

Business

Requirements
Must have
• *Details on all cards*

Company Name: Tallobrix Pty Ltd
ABN: 52 683 914 207
Address: 47-49 Pembury Street, Ashcombe Vale, Victoria 3172
Phone: 1300 GRAB UP
Fax: 03 9417 6258
Website: www.tallobrix.com.au
Logo/Handprint Icon

*Person Specific*

```html
<!DOCTYPE html>
<html lang="en">
<head>
<meta charset="utf-8">
<title>Tallobrix Business Cards</title>
<link rel="stylesheet" href="https://fonts.googleapis.com/css2?family=Cinzel:wght@400;600&display=swap">
<style>
  :root {
    --stage-dark: #0c0c0c;
    --stage-mid: #7a7a7a;
    --card-light: #e6e6e6;
    --card-blue: #4a86b4;
    --card-blue-soft: #4f8abb;
    --card-navy: #24465f;
    --ink-dark: #333333;
    --ink-white: #ffffff;
    --ink-soft: #dce9f4;
    --mark-blue: #2f6aa3;
  }
  * { margin: 0; padding: 0; box-sizing: border-box; }
  html, body { width: 1200px; height: 1069px; overflow: hidden; }
  body {
    position: relative;
    font-family: "Cinzel", "Times New Roman", serif;
    background: radial-gradient(ellipse 620px 560px at 600px 530px, var(--stage-mid) 0%, #3a3a3a 55%, var(--stage-dark) 100%);
  }
  .card { position: absolute; overflow: hidden; box-shadow: 0 10px 22px rgba(0,0,0,.55); }
  .card--front-light { left: 80px; top: 184px; width: 474px; height: 271px; background: var(--card-light); }
  .card--back-blue { left: 638px; top: 189px; width: 462px; height: 263px; background: var(--card-blue); }
  .card--front-navy { left: 103px; top: 670px; width: 474px; height: 269px; background: var(--card-navy); border-radius: 16px; }
  .card--back-rounded { left: 660px; top: 674px; width: 461px; height: 262px; border-radius: 16px;
    background: var(--card-blue-soft); }
  .stripes { position: absolute; inset: 0; }

  .wordmark { position: absolute; font-weight: 400; letter-spacing: 1px; white-space: nowrap; }
  .wordmark--light { left: 102px; top: 104px; font-size: 54px; color: var(--ink-dark); }
  .wordmark--navy { left: 70px; top: 100px; font-size: 54px; color: var(--ink-white); }
  .wordmark--corner { right: 30px; top: 32px; font-size: 22px; color: var(--ink-white); }
  .wordmark-shadow { position: absolute; height: 6px; border-radius: 50%; background: rgba(0,0,0,.25); }
  .wordmark-shadow--light { left: 110px; top: 184px; width: 60px; }
  .wordmark-shadow--navy { left: 102px; top: 184px; width: 60px; background: rgba(0,0,0,.35); }

  .mark-area { position: absolute; border-radius: 50%; }
  .mark-area--back { left: 14px; top: 128px; width: 120px; height: 120px; background: radial-gradient(circle, rgba(34,90,160,.55), rgba(34,90,160,0) 70%); }
  .mark-area--navy { left: 250px; top: 50px; width: 200px; height: 200px; background: radial-gradient(circle, rgba(255,255,255,.09), rgba(255,255,255,0) 70%); }
  .mark-area--rounded { left: 30px; top: 120px; width: 130px; height: 130px; background: radial-gradient(circle, rgba(255,255,255,.18), rgba(255,255,255,0) 70%); }

  .person { position: absolute; color: var(--ink-white); }
  .person__name { font-size: 19px; letter-spacing: .5px; }
  .person__field { font-size: 11px; line-height: 17px; }
  .person--back { left: 50px; top: 32px; }
  .person--back .person__name { margin-bottom: 6px; }
  .person--rounded { left: 41px; top: 22px; }
  .person--rounded .person__name { font-size: 24px; margin-bottom: 4px; }
  .person--rounded .person__field { font-size: 13px; line-height: 20px; }

  .divider { position: absolute; left: 212px; top: 137px; width: 2px; height: 114px; background: var(--ink-white); }

  .company { position: absolute; color: var(--ink-white); }
  .company__name { font-size: 27px; white-space: nowrap; }
  .company__name small { font-size: 13px; }
  .company__details { list-style: none; margin-top: 6px; font-size: 8.5px; line-height: 11px; color: var(--ink-soft); }
  .company--back { left: 230px; top: 146px; }
  .company--rounded { left: 208px; top: 136px; }
  .company--rounded .company__details li::before {
    content: ""; display: inline-block; width: 5px; height: 5px; border-radius: 50%;
    background: var(--ink-soft); margin-right: 4px; vertical-align: middle;
  }
</style>
</head>
<body>

  <section class="card card--front-light" aria-label="Card front, light">
    <span class="wordmark wordmark--light">Tallobrix</span>
    <span class="wordmark-shadow wordmark-shadow--light"></span>
  </section>

  <section class="card card--back-blue" aria-label="Card back, blue">
    <div class="person person--back">
      <p class="person__name">DANIEL HARWOOD</p>
      <p class="person__field">MOB#</p>
      <p class="person__field">EMAIL ID:</p>
    </div>
    <div class="mark-area mark-area--back" role="img" aria-label="Brand mark area"></div>
    <span class="divider"></span>
    <div class="company company--back">
      <p class="company__name">Tallobrix <small>PTY LTD</small></p>
      <ul class="company__details">
        <li>ABN: 52 683 914 207</li>
        <li>47-49 PEMBURY STREET, ASHCOMBE VALE</li>
        <li>VICTORIA 3172</li>
        <li>PH# 1300 GRAB UP</li>
        <li>FAX: 03 9417 6258</li>
        <li>WWW.TALLOBRIX.COM.AU</li>
      </ul>
    </div>
  </section>

  <section class="card card--front-navy" aria-label="Card front, navy">
    <div class="mark-area mark-area--navy" role="img" aria-label="Faint brand mark decoration"></div>
    <span class="wordmark wordmark--navy">Tallobrix</span>
    <span class="wordmark-shadow wordmark-shadow--navy"></span>
  </section>

  <section class="card card--back-rounded" aria-label="Card back, rounded">
    <svg class="stripes" width="461" height="262" aria-hidden="true">
      <g stroke="rgba(255,255,255,.12)" stroke-width="1">
        <line x1="120" y1="262" x2="461" y2="60"/>
        <line x1="40" y1="262" x2="461" y2="12"/>
        <line x1="200" y1="262" x2="461" y2="108"/>
        <line x1="0" y1="200" x2="340" y2="0"/>
      </g>
    </svg>
    <div class="person person--rounded">
      <p class="person__name">Daniel Harwood</p>
      <p class="person__field">Mob#</p>
      <p class="person__field">Email id:</p>
    </div>
    <span class="wordmark wordmark--corner">Tallobrix</span>
    <div class="mark-area mark-area--rounded" role="img" aria-label="Faint brand mark decoration"></div>
    <div class="company company--rounded">
      <p class="company__name">Tallobrix <small>PTY LTD</small></p>
      <ul class="company__details">
        <li>ABN: 52 683 914 207</li>
        <li>47-49 PEMBURY STREET, ASHCOMBE VALE, VICTORIA 3172</li>
        <li>PH# 1300 GRAB UP</li>
        <li>FAX: 03 9417 6258</li>
        <li>WWW.TALLOBRIX.COM.AU</li>
      </ul>
    </div>
  </section>

</body>
</html>
```